Business Card for Makeup Artist

I need a business card designed for my makeup and hair artistry business which is primarily events and weddings focused. The card needs to be sleek, simple, stylish and appealing to women. I would prefer a white background but open to suggestions also. I also love the marble background look. I have attached some example pics. It needs to be a double sided card with logo and/or design on one side and contact details in the centre of the card on the other side. NO LOGO ON BACK. Examples attached.

Target Market(s)

Females age 14-55

Industry/Entity Type

Business

Contact Information for Business Card

Nora Vint
Principal Makeup Artist
P: 0413 925 214
E: nora@lumirabeauty.com.au
W: www.lumirabeauty.com.au

Requirements
Should not have
• No yellow, green, red or blue in the design.

```html
<!DOCTYPE html>
<html lang="en">
<head>
<meta charset="utf-8">
<title>Lumira Makeup Artistry – Business Card</title>
<link rel="stylesheet" href="https://fonts.googleapis.com/css2?family=Cormorant+SC:wght@400;500&family=Great+Vibes&family=Raleway:wght@300&display=swap">
<style>
  :root {
    --stage: #e6e6e6;
    --card: #ffffff;
    --ink: #5e5e5e;
    --ink-soft: #7a7a7a;
    --rule: #9a9a9a;
    --brush-dark: #6b5a50;
    --brush-mid: #a08a7c;
    --brush-light: #d9cdc4;
    --brush-pink: #d98aa8;
  }
  * { box-sizing: border-box; margin: 0; padding: 0; }
  html, body {
    width: 1200px;
    height: 596px;
    overflow: hidden;
    background: var(--stage);
  }
  .stage {
    width: 1200px;
    height: 596px;
    display: flex;
    align-items: center;
    justify-content: center;
    gap: 40px;
  }
  .card {
    position: relative;
    width: 540px;
    height: 300px;
    background: var(--card);
    overflow: hidden;
    box-shadow: 0 2px 10px rgba(0,0,0,0.12);
  }
  .brush-row {
    position: absolute;
    left: 40px;
    right: 40px;
    bottom: 0;
    height: 112px;
    background:
      linear-gradient(to bottom, rgba(255,255,255,0.9) 0%, rgba(255,255,255,0) 45%),
      linear-gradient(to right,
        var(--brush-mid) 0%, var(--brush-light) 12%, var(--brush-dark) 22%,
        var(--brush-light) 32%, var(--brush-pink) 44%, var(--brush-mid) 55%,
        var(--brush-light) 66%, var(--brush-dark) 78%, var(--brush-light) 88%,
        var(--brush-mid) 100%);
    opacity: 0.55;
  }
  .card--back .brush-row { opacity: 0.4; }

  /* Front */
  .brand {
    position: absolute;
    top: 62px;
    left: 0;
    right: 0;
    text-align: center;
    font-family: "Raleway", sans-serif;
    font-weight: 300;
    color: var(--ink);
    line-height: 1;
  }
  .brand__name {
    display: block;
    font-size: 66px;
    letter-spacing: 4px;
  }
  .brand__tagline {
    display: block;
    margin-top: 10px;
    font-size: 22px;
    letter-spacing: 2px;
    text-transform: uppercase;
  }

  /* Back */
  .contact {
    position: absolute;
    top: 30px;
    left: 0;
    right: 0;
    text-align: center;
    color: var(--ink);
    z-index: 1;
  }
  .contact__name {
    font-family: "Great Vibes", cursive;
    font-weight: 400;
    font-size: 34px;
    line-height: 1.1;
    color: var(--ink-soft);
  }
  .contact__title {
    display: inline-block;
    margin-top: 6px;
    padding: 0 36px 5px;
    border-bottom: 1px solid var(--rule);
    font-family: "Cormorant SC", serif;
    font-size: 19px;
    letter-spacing: 1.5px;
  }
  .contact__list {
    list-style: none;
    margin-top: 22px;
    font-family: "Cormorant SC", serif;
    font-size: 18px;
    line-height: 1.45;
    letter-spacing: 1px;
  }
</style>
</head>
<body>
  <main class="stage">
    <section class="card card--front" aria-label="Card front">
      <h1 class="brand">
        <span class="brand__name">Lumira</span>
        <span class="brand__tagline">Makeup Artistry</span>
      </h1>
      <div class="brush-row" role="img" aria-label="Watercolour illustration of a row of makeup brushes"></div>
    </section>

    <section class="card card--back" aria-label="Card back">
      <div class="brush-row" role="img" aria-label="Watercolour illustration of a row of makeup brushes"></div>
      <div class="contact">
        <h2 class="contact__name">Nora Vint</h2>
        <p class="contact__title">Principal Makeup Artist</p>
        <ul class="contact__list">
          <li>P: 0413 925 214</li>
          <li>E: nora@lumirabeauty.com.au</li>
          <li>W: www.lumirabeauty.com.au</li>
        </ul>
      </div>
    </section>
  </main>
</body>
</html>
```